Financial firm simple design

Classic business card design for a financial fund. 2 sided card- white on both sides.. One with just the company name centered and the other w the info. info included on that is :

Name
Company position
phone number
fax
email
website

Financial

```html
<!DOCTYPE html>
<html lang="en">
<head>
<meta charset="utf-8">
<title>Harlow Capital – Business Card</title>
<link rel="stylesheet" href="https://fonts.googleapis.com/css2?family=EB+Garamond:wght@400;700&family=Source+Code+Pro:wght@500&display=swap">
<style>
  :root {
    --backdrop: #b4b6ba;
    --card: #fdfdfb;
    --navy: #1c3f73;
    --ink: #1f1f22;
  }
  html, body {
    margin: 0;
    width: 1200px;
    height: 1200px;
    overflow: hidden;
    background: var(--backdrop);
  }
  .stage {
    position: relative;
    width: 1200px;
    height: 1200px;
  }
  .card {
    position: absolute;
    left: 229px;
    width: 743px;
    height: 422px;
    background: var(--card);
    box-shadow: 0 1px 3px rgba(0,0,0,0.12);
  }
  .card--front { top: 166px; }
  .card--back  { top: 598px; }

  .wordmark {
    position: absolute;
    font-family: "EB Garamond", serif;
    font-weight: 400;
    font-size: 38px;
    letter-spacing: 0.06em;
    color: var(--navy);
    white-space: nowrap;
    line-height: 1;
  }
  .card--front .wordmark {
    left: 0;
    right: 0;
    top: 183px;
    text-align: center;
  }
  .card--back .wordmark {
    left: 37px;
    top: 92px;
  }

  .front-url {
    position: absolute;
    left: 0;
    right: 0;
    top: 373px;
    text-align: center;
    font-family: "EB Garamond", serif;
    font-size: 24px;
    letter-spacing: 1.12em;
    padding-left: 1.12em;
    color: var(--navy);
    line-height: 1;
  }

  .holder {
    position: absolute;
    left: 83px;
    top: 268px;
    font-family: "EB Garamond", serif;
  }
  .holder__name {
    margin: 0;
    font-weight: 700;
    font-size: 27px;
    color: var(--navy);
    line-height: 1.2;
  }
  .holder__role {
    margin: 2px 0 0;
    font-size: 24px;
    color: var(--ink);
    line-height: 1.2;
  }

  .contacts {
    position: absolute;
    left: 406px;
    top: 272px;
    margin: 0;
    padding: 0;
    list-style: none;
  }
  .contacts__item {
    display: flex;
    align-items: center;
    height: 30.5px;
  }
  .contacts__icon {
    width: 24px;
    height: 24px;
    margin-right: 11px;
    flex: none;
  }
  .contacts__text {
    font-family: "EB Garamond", serif;
    font-size: 23px;
    color: var(--ink);
  }
  .contacts__text--number {
    font-family: "Source Code Pro", monospace;
    font-size: 21px;
    letter-spacing: 0.04em;
    word-spacing: 0.2em;
  }
</style>
</head>
<body>
<main class="stage">

  <section class="card card--front" aria-label="Card front">
    <div class="wordmark">HARLOW CAPITAL</div>
    <div class="front-url">www.yourdomain.com</div>
  </section>

  <section class="card card--back" aria-label="Card back">
    <div class="wordmark">HARLOW CAPITAL</div>

    <div class="holder">
      <p class="holder__name">Your Name</p>
      <p class="holder__role">Company position</p>
    </div>

    <ul class="contacts">
      <li class="contacts__item">
        <svg class="contacts__icon" viewBox="0 0 24 24" aria-label="Phone">
          <circle cx="12" cy="12" r="12" fill="var(--navy)"/>
          <path d="M7.5 8.5c0-1 1-2 2-2l1.5 2.5-1 1.2c.6 1.5 1.8 2.7 3.3 3.3l1.2-1 2.5 1.5c0 1-1 2-2 2-4 0-7.5-3.5-7.5-7.5z" fill="#fff"/>
        </svg>
        <span class="contacts__text contacts__text--number">5555 555 555</span>
      </li>
      <li class="contacts__item">
        <svg class="contacts__icon" viewBox="0 0 24 24" aria-label="Fax">
          <circle cx="12" cy="12" r="12" fill="var(--navy)"/>
          <rect x="8.5" y="5" width="7" height="4" fill="#fff"/>
          <rect x="5.5" y="9.5" width="13" height="7" rx="1" fill="#fff"/>
          <rect x="8.5" y="14" width="7" height="4.5" fill="#fff" stroke="var(--navy)" stroke-width="1"/>
        </svg>
        <span class="contacts__text contacts__text--number">5555 555 555</span>
      </li>
      <li class="contacts__item">
        <svg class="contacts__icon" viewBox="0 0 24 24" aria-label="Email">
          <circle cx="12" cy="12" r="12" fill="var(--navy)"/>
          <rect x="5.5" y="7.5" width="13" height="9" fill="#fff"/>
          <path d="M5.5 7.5l6.5 5 6.5-5M5.5 16.5l4.5-4.5M18.5 16.5l-4.5-4.5" fill="none" stroke="var(--navy)" stroke-width="1.2"/>
        </svg>
        <span class="contacts__text">name@yourdomain.com</span>
      </li>
      <li class="contacts__item">
        <svg class="contacts__icon" viewBox="0 0 24 24" aria-label="Website">
          <circle cx="12" cy="12" r="12" fill="var(--navy)"/>
          <g fill="none" stroke="#fff" stroke-width="1.2">
            <circle cx="12" cy="12" r="7"/>
            <ellipse cx="12" cy="12" rx="3" ry="7"/>
            <path d="M5 12h14M6.2 8.5h11.6M6.2 15.5h11.6"/>
          </g>
        </svg>
        <span class="contacts__text">www.yourdomain.com</span>
      </li>
    </ul>
  </section>

</main>
</body>
</html>
```